Pelin Thai Massage Double Sided Flyer Luxury

I require a double sided flyer
we are a Thai Massage Spa
Would like gold, deep purple and bronze colours
Something eye catching and looks professional

```html
<!DOCTYPE html>
<html lang="en">
<head>
<meta charset="utf-8">
<title>Pelin Thai Massage – Double Sided Flyer</title>
<link rel="stylesheet" href="https://fonts.googleapis.com/css2?family=Marcellus&family=Marcellus+SC&family=Poppins:wght@400;500&family=Pinyon+Script&display=swap">
<style>
  :root {
    --gold: #f7c24a;
    --gold-soft: #fbd77e;
    --purple: #5b2a7e;
    --purple-text: #5e2d85;
    --bronze: #a8703f;
    --paper: #ffffff;
    --backdrop: #e6e6e8;
    --rule: #b9a6c9;
  }
  * { margin: 0; padding: 0; box-sizing: border-box; }
  html, body { width: 1200px; height: 782px; overflow: hidden; }
  body {
    background: var(--backdrop);
    position: relative;
    font-family: "Poppins", sans-serif;
    color: var(--purple-text);
  }
  .flyer {
    position: absolute;
    top: 26px;
    width: 515px;
    height: 730px;
    background: var(--paper);
    overflow: hidden;
  }
  .flyer--front { left: 55px; }
  .flyer--back { left: 630px; }
  .abs { position: absolute; }

  /* Front */
  .brand-mark {
    left: 164px; top: 32px;
    width: 188px; height: 188px;
    border-radius: 50%;
    border: 6px solid var(--gold);
  }
  .brand-name {
    left: 0; width: 100%; top: 220px;
    text-align: center;
    font-family: "Marcellus", serif;
    font-size: 36px;
    color: var(--gold);
  }
  .welcome {
    left: 0; width: 100%; top: 284px;
    text-align: center;
    font-family: "Marcellus SC", serif;
    font-size: 25px;
    letter-spacing: 1px;
    color: var(--gold);
  }
  .intro {
    left: 24px; width: 467px;
    text-align: center;
    font-size: 12.6px;
    line-height: 17px;
    color: var(--purple-text);
  }
  .intro--one { top: 329px; }
  .intro--two { top: 407px; }
  .divider-dots { left: 245px; top: 391px; width: 26px; height: 6px; }
  .front-photo {
    left: 0; bottom: 0; width: 100%; height: 262px;
    background: linear-gradient(160deg, #ffffff 0%, #f6e6dc 35%, #efd2c3 60%, #f9f4f4 85%, #ffffff 100%);
  }

  /* Back */
  .header-band {
    left: 15px; top: 0; width: 484px; height: 111px;
    background: var(--purple);
    border-radius: 0 0 10px 10px;
    text-align: center;
    color: #fff;
  }
  .header-band h1 {
    font-family: "Marcellus", serif;
    font-weight: 400;
    font-size: 34px;
    color: var(--gold);
    margin-top: 12px;
    line-height: 40px;
  }
  .header-band p {
    font-size: 13px;
    line-height: 18.5px;
    margin-top: 4px;
    padding: 0 12px;
  }
  .back-photo {
    left: 255px; top: 176px; width: 260px; height: 554px;
    background:
      radial-gradient(ellipse at 85% 35%, rgba(236,96,140,0.55) 0%, rgba(236,96,140,0) 35%),
      radial-gradient(ellipse at 70% 18%, #efe9e2 0%, rgba(239,233,226,0) 45%),
      linear-gradient(90deg, rgba(255,255,255,1) 0%, rgba(245,245,245,0.6) 40%, #ececec 100%);
  }
  .section-title {
    left: 32px; top: 128px;
    font-size: 27px;
    font-weight: 400;
    color: var(--purple);
  }
  .category {
    left: 32px;
    font-size: 15px;
    font-weight: 500;
    color: var(--bronze);
  }
  .category--deep { top: 161px; }
  .category--thai { top: 365px; }
  .treatment { left: 34px; display: flex; align-items: center; gap: 14px; }
  .treatment--one { top: 202px; }
  .treatment--two { top: 284px; }
  .treatment--three { top: 410px; }
  .treatment-dot {
    width: 52px; height: 52px; border-radius: 50%;
    border: 3px solid var(--gold);
    flex: none;
  }
  .treatment-text { font-size: 13.8px; line-height: 19.6px; color: var(--purple-text); }
  .treatment-text .price { color: var(--bronze); }
  .contact-rule { left: 30px; top: 492px; width: 332px; height: 1px; background: var(--rule); }
  .contact-line { left: 33px; display: flex; align-items: center; gap: 9px; color: var(--purple); }
  .contact-line svg { flex: none; }
  .contact-phone { top: 510px; font-size: 23px; font-weight: 500; }
  .contact-web { top: 538px; font-size: 15px; }
  .contact-address { top: 570px; font-size: 15px; line-height: 19.5px; align-items: flex-start; }
  .gift-note {
    left: 52px; top: 636px;
    font-family: "Pinyon Script", cursive;
    font-size: 22px;
    color: var(--bronze);
  }
  .open-bar {
    left: 0; top: 693px; width: 209px; height: 23px;
    background: var(--purple);
    border-radius: 0 12px 12px 0;
    color: #fff;
    font-size: 13.5px;
    font-weight: 500;
    text-align: center;
    line-height: 23px;
    padding-left: 14px;
  }
</style>
</head>
<body>

<section class="flyer flyer--front">
  <div class="abs brand-mark"></div>
  <div class="abs brand-name">Pelin Thai Massage</div>
  <h2 class="abs welcome">Welcome to Luxury</h2>
  <p class="abs intro intro--one">Set in the heart of Roundhay, Pelin Thai Massage will allow you to immerse yourself in a place where your wellbeing and rejuvenation is at the centre of what we do.</p>
  <svg class="abs divider-dots" viewBox="0 0 26 6" aria-hidden="true">
    <circle cx="3" cy="3" r="2" fill="var(--gold)"/>
    <circle cx="13" cy="3" r="3" fill="var(--gold)"/>
    <circle cx="23" cy="3" r="2" fill="var(--gold)"/>
  </svg>
  <p class="abs intro intro--two">Using Thai traditions, our highly trained therapists offer revitalising body treatments with their deep tissue massage techniques. In their hands, you will see and feel immediate results.</p>
  <div class="abs front-photo" role="img" aria-label="Photo of a relaxed client receiving a head massage on a white towel with pink orchids"></div>
</section>

<section class="flyer flyer--back">
  <header class="abs header-band">
    <h1>Massages</h1>
    <p>Restore balance. Revive your senses. Discover all the ways Pelin Thai Massage can breathe new life into your body and soul.</p>
  </header>

  <div class="abs back-photo" role="img" aria-label="Spa still life with bath salts in a white mortar, pink lily, white pebbles and a rolled towel"></div>

  <h2 class="abs section-title">MASSAGES</h2>
  <h3 class="abs category category--deep">DEEP TISSUE MASSAGE</h3>

  <div class="abs treatment treatment--one">
    <div class="treatment-dot"></div>
    <div class="treatment-text"><span class="price">60 minutes £45</span><br>Oil massage personalised,<br>light to firm pressure</div>
  </div>
  <div class="abs treatment treatment--two">
    <div class="treatment-dot"></div>
    <div class="treatment-text"><span class="price">90 minutes £55</span><br>Oil massage<br>medium to firm pressure</div>
  </div>

  <h3 class="abs category category--thai">THAI FLOOR TRADTIONAL MASSAGE</h3>
  <div class="abs treatment treatment--three">
    <div class="treatment-dot"></div>
    <div class="treatment-text"><span class="price">60 minutes £45</span><br>Dry massage, medium to firm pressure<br>applying stretching technique</div>
  </div>

  <div class="abs contact-rule"></div>

  <div class="abs contact-line contact-phone">
    <svg width="20" height="20" viewBox="0 0 20 20" aria-hidden="true">
      <circle cx="10" cy="10" r="10" fill="var(--gold)"/>
      <path d="M7 5.5l1.6 2.3-1 1.2c.6 1.3 1.5 2.2 2.7 2.8l1.2-1 2.3 1.5-.7 1.9c-3.7-.3-6.6-3.2-6.9-6.9z" fill="#fff"/>
    </svg>
    <span>0113 496 0732</span>
  </div>
  <div class="abs contact-line contact-web">
    <svg width="20" height="20" viewBox="0 0 20 20" aria-hidden="true">
      <circle cx="10" cy="10" r="10" fill="var(--gold)"/>
      <circle cx="10" cy="10" r="5.5" fill="none" stroke="#fff" stroke-width="1.2"/>
      <ellipse cx="10" cy="10" rx="2.4" ry="5.5" fill="none" stroke="#fff" stroke-width="1.2"/>
      <line x1="4.5" y1="10" x2="15.5" y2="10" stroke="#fff" stroke-width="1.2"/>
    </svg>
    <span>www.pelinthaimassage.co.uk</span>
  </div>
  <div class="abs contact-line contact-address">
    <svg width="20" height="20" viewBox="0 0 20 20" aria-hidden="true">
      <circle cx="10" cy="10" r="10" fill="var(--gold)"/>
      <path d="M10 4.5a3.8 3.8 0 0 0-3.8 3.8c0 2.8 3.8 7 3.8 7s3.8-4.2 3.8-7A3.8 3.8 0 0 0 10 4.5z" fill="#fff"/>
      <circle cx="10" cy="8.3" r="1.4" fill="var(--gold)"/>
    </svg>
    <span>Pelin Thai Massage<br>42 Oakwood Road<br>Leeds, LS8 2QT</span>
  </div>

  <div class="abs gift-note">Gift Vouchers Available</div>
  <div class="abs open-bar">Open 7 Days a Week</div>
</section>

</body>
</html>
```